Business Card for a Floral & Decorating Business

I would like to take my current logo and create a better business card. I am looking for elegance as I am a florist and event decorator. My logo has multiple colour options. I like colours like green, purple, pink and orange, I think I would like a white card, open to black back ground. I want it to feel elegant and romantic. I like metallic lettering that maybe is indented in the paper, I also like glossy paper. I have a full logo already as well as a badge. I have attached both in multiple colours.m

Target Market(s)

Weddings, special events, floral customers

Industry/Entity Type

Floral and decorating

Contact Information for Business Card

Phone number, email, instagram, facebook, title, name, logo

Font styles to use
Script

Requirements
Nice to have
• Elegant

```html
<!DOCTYPE html>
<html lang="en">
<head>
<meta charset="utf-8">
<title>Marlow Hensley — Business Card</title>
<link rel="stylesheet" href="https://fonts.googleapis.com/css2?family=Lora:wght@400;500&family=Lato:wght@400&display=swap">
<style>
  :root {
    --bg: #ecebe8;
    --paper: #ffffff;
    --paper-shade: #f1f1f0;
    --sage: #4f8a79;
    --sage-deep: #3d7465;
    --berry: #9a3a5c;
    --forest: #24463f;
    --forest-light: #5f8c82;
    --forest-line: #1f3d37;
  }
  * { margin: 0; padding: 0; box-sizing: border-box; }
  html, body { width: 1200px; height: 960px; overflow: hidden; }
  body {
    background: var(--bg);
    display: flex;
    flex-direction: column;
    align-items: center;
    justify-content: center;
    gap: 56px;
  }
  .card {
    position: relative;
    width: 700px;
    height: 400px;
    box-shadow: 0 10px 28px rgba(0,0,0,.16);
    overflow: hidden;
  }

  /* Front */
  .card--front {
    background: linear-gradient(160deg, var(--paper-shade) 0%, var(--paper) 45%, var(--paper-shade) 100%);
  }
  .brand {
    position: absolute;
    left: 70px;
    top: 70px;
    display: flex;
    flex-direction: column;
    gap: 10px;
    color: var(--sage);
  }
  .brand__row { display: flex; align-items: center; gap: 14px; }
  .brand__mark {
    width: 20px; height: 20px;
    border-radius: 50%;
    background: var(--sage);
  }
  .brand__name {
    font-family: 'Lora', serif;
    font-weight: 400;
    font-size: 40px;
    letter-spacing: .5px;
    color: var(--sage);
  }
  .brand__tagline {
    font-family: 'Lora', serif;
    font-size: 11px;
    letter-spacing: 4px;
    text-transform: uppercase;
    color: var(--sage);
    padding-left: 34px;
  }
  .divider {
    position: absolute;
    left: 372px;
    top: 180px;
    width: 1.5px;
    height: 62px;
    background: var(--berry);
  }
  .person {
    position: absolute;
    left: 394px;
    top: 184px;
  }
  .person__name {
    font-family: 'Lora', serif;
    font-weight: 500;
    font-size: 26px;
    letter-spacing: 3px;
    color: var(--sage-deep);
    text-transform: uppercase;
  }
  .person__title {
    font-family: 'Lora', serif;
    font-size: 17px;
    color: var(--sage);
    margin-top: 2px;
  }
  .contacts {
    position: absolute;
    left: 300px;
    top: 268px;
    list-style: none;
    display: flex;
    flex-direction: column;
    gap: 6px;
  }
  .contacts__item {
    display: flex;
    align-items: center;
    gap: 12px;
    font-family: 'Lato', sans-serif;
    font-size: 16px;
    color: var(--berry);
  }
  .contacts__icon {
    width: 18px; height: 18px;
    flex: none;
    color: var(--sage);
  }
  .contacts__badge {
    width: 16px; height: 16px;
    flex: none;
    margin: 1px;
    background: var(--sage);
    border-radius: 3px;
  }
  .contacts__badge--round { border-radius: 50%; background: none; border: 1.6px solid var(--sage); }

  /* Back */
  .card--back {
    background: radial-gradient(ellipse at 30% 40%, var(--forest-light) 0%, var(--forest) 85%);
  }
  .back-floral {
    position: absolute;
    right: 0;
    top: 40px;
    width: 230px;
    height: 360px;
    background: radial-gradient(ellipse at 60% 55%, rgba(31,61,55,.55) 0%, rgba(31,61,55,0) 70%);
  }
  .back-brand {
    position: absolute;
    left: 250px;
    top: 150px;
    text-align: right;
  }
  .back-brand__name {
    font-family: 'Lora', serif;
    font-size: 40px;
    color: var(--forest-line);
    letter-spacing: .5px;
  }
  .back-brand__tagline {
    font-family: 'Lora', serif;
    font-size: 11px;
    letter-spacing: 4px;
    text-transform: uppercase;
    color: var(--forest-line);
    margin-top: 6px;
  }
</style>
</head>
<body>

  <section class="card card--front" aria-label="Card front">
    <div class="brand">
      <div class="brand__row">
        <span class="brand__mark"></span>
        <span class="brand__name">marlow hensley</span>
      </div>
      <span class="brand__tagline">Decorating &amp; Florals.</span>
    </div>

    <span class="divider"></span>

    <div class="person">
      <p class="person__name">Marlow Hensley</p>
      <p class="person__title">Events Designer</p>
    </div>

    <ul class="contacts">
      <li class="contacts__item">
        <svg class="contacts__icon" viewBox="0 0 18 18" fill="none" stroke="currentColor" stroke-width="1.4">
          <rect x="5" y="1.5" width="8" height="15" rx="1.5"/>
          <line x1="8" y1="14" x2="10" y2="14"/>
        </svg>
        555-014-2290
      </li>
      <li class="contacts__item">
        <svg class="contacts__icon" viewBox="0 0 18 18" fill="none" stroke="currentColor" stroke-width="1.4">
          <rect x="1.5" y="4" width="15" height="10" rx="1"/>
          <polyline points="1.5,4 9,10 16.5,4"/>
        </svg>
        info@marlowhensley.com
      </li>
      <li class="contacts__item">
        <span class="contacts__badge contacts__badge--round"></span>
        @fondlymarlow22
      </li>
      <li class="contacts__item">
        <span class="contacts__badge"></span>
        @fondlykeptdecor
      </li>
    </ul>
  </section>

  <section class="card card--back" aria-label="Card back">
    <div class="back-floral" role="img" aria-label="Line-drawn peonies and leaves in dark green along the right edge"></div>
    <div class="back-brand">
      <p class="back-brand__name">marlow hensley</p>
      <p class="back-brand__tagline">Fondly Kept</p>
    </div>
  </section>

</body>
</html>
```